Vantrell Law Letterhead

We need a new letterhead design for a Law Firm. The address for the law firm is 4817 Larkspur Boulevard, Suite 250, Houston, Texas 77342. Phone Number: 832-619-3057; Fax Number: 832-407-1694. The logo is uploaded to the project.

```html
<!DOCTYPE html>
<html lang="en">
<head>
<meta charset="utf-8">
<title>Vantrell Law Letterhead</title>
<link href="https://fonts.googleapis.com/css2?family=Arimo:wght@400;700&display=swap" rel="stylesheet">
<style>
  :root {
    --navy: #1d3576;
    --red: #c8202a;
    --ink: #1c1c1c;
    --paper: #ffffff;
    --backdrop: #262626;
  }
  * { margin: 0; padding: 0; box-sizing: border-box; }
  html, body { width: 1200px; height: 800px; overflow: hidden; background: var(--backdrop); }
  body { position: relative; font-family: "Arimo", Arial, sans-serif; }

  .letterhead {
    position: absolute; left: 306px; top: 20px;
    width: 588px; height: 760px;
    background: var(--paper);
  }

  .brand {
    position: absolute; left: 30px; top: 34px;
    display: flex; align-items: center; gap: 12px;
  }
  .brand-mark { width: 40px; height: 40px; background: var(--navy); }
  .brand-name {
    font-size: 32px; font-weight: 400; color: var(--navy);
    letter-spacing: 0.5px; line-height: 1;
  }

  .address {
    position: absolute; right: 24px; top: 82px;
    text-align: right; color: var(--navy);
    font-size: 13.5px; line-height: 19px; text-transform: uppercase;
  }

  .rule { position: absolute; left: 0; width: 100%; }
  .rule-navy { height: 3px; background: var(--navy); }
  .rule-red { height: 2px; background: var(--red); }
  .header-rule.rule-navy { top: 126px; }
  .header-rule.rule-red { top: 131px; }
  .footer-rule.rule-navy { top: 694px; }
  .footer-rule.rule-red { top: 699px; }

  .letter {
    position: absolute; left: 77px; top: 200px; width: 460px;
    font-size: 11.6px; line-height: 20.1px; color: var(--ink);
  }
  .salutation { margin-bottom: 20px; }
  .body-text { margin-bottom: 20px; }
  .closing { margin-bottom: 20px; }

  .contacts {
    position: absolute; top: 716px; left: 88px;
    display: flex; gap: 52px;
  }
  .contact { display: flex; align-items: center; gap: 10px; color: var(--ink); font-size: 20px; }
  .contact svg { width: 27px; height: 27px; display: block; }
</style>
</head>
<body>
<main class="letterhead">
  <header>
    <div class="brand">
      <span class="brand-mark"></span>
      <span class="brand-name">Vantrell Law</span>
    </div>
    <address class="address">
      4817 Larkspur Boulevard<br>
      Suite 250, Houston, Texas 77342
    </address>
  </header>
  <div class="rule rule-navy header-rule"></div>
  <div class="rule rule-red header-rule"></div>

  <section class="letter">
    <p class="salutation">Dear; Person Name</p>
    <p class="body-text">
      Lorem ipsum dolor sit amet, consectetur adipiscing elit. Aenean ut ipsum eget massa<br>
      .hendrerit vestibulum vel in velit. Donec pretium neque velit<br>
      Aliquam porta lectus nec mauris ornare venenatis. Vivamus non est turpis, et cursus<br>
      .sem. Mauris vehicula erat in diam auctor at bibendum nisl lacinia<br>
      Morbi imperdiet neque vehicula nunc convallis gravida. Vestibulum iaculis pretium<br>
      placerat. Integer consequat, est sit amet facilisis eleifend, nibh nibh varius orci, eget<br>
      dapibus arcu dui non purus. Pellentesque in magna mauris. Duis enim sapien, dictum<br>
      vitae condimentum a, pulvinar vel lacus. Mauris et molestie nibh. Vestibulum vitae<br>
      nulla at metus elementum porta sit amet interdum elit. Nulla sollicitudin neque eu nulla<br>
      .volutpat congue<br>
      Etiam pellentesque, velit id dapibus fermentum, turpis sapien ornare dui, ac tincidunt<br>
      ligula odio congue purus. Nunc sed ante dui, in porta lectus. Cras nec sem lorem. In<br>
      hac habitasse platea dictumst. Maecenas id diam quis dui porta tristique. Sed id<br>
      egestas felis. Donec ullamcorper mattis posuere. Phasellus fermentum eleifend tortor<br>
      .vel dapibus. Vestibulum ante ipsum
    </p>
    <p class="closing">,Sincerely</p>
    <p class="signature">Sender Name</p>
  </section>

  <div class="rule rule-navy footer-rule"></div>
  <div class="rule rule-red footer-rule"></div>
  <footer class="contacts">
    <div class="contact contact-phone">
      <svg viewBox="0 0 32 32" aria-hidden="true">
        <circle cx="16" cy="16" r="16" fill="var(--red)"/>
        <path d="M11.5 8.5l3 3-1.6 2.1c.9 1.9 2.4 3.4 4.3 4.3l2.1-1.6 3 3-2 2.2c-4.8-.6-9.7-5.5-10.3-10.3z" fill="#fff"/>
      </svg>
      <span>832-619-3057</span>
    </div>
    <div class="contact contact-fax">
      <svg viewBox="0 0 32 32" aria-hidden="true">
        <circle cx="16" cy="16" r="16" fill="var(--red)"/>
        <rect x="11" y="8" width="10" height="5" fill="#fff"/>
        <rect x="8" y="13" width="16" height="8" rx="1.5" fill="#fff"/>
        <rect x="11" y="19" width="10" height="5" fill="#fff" stroke="var(--red)" stroke-width="1"/>
      </svg>
      <span>832-407-1694</span>
    </div>
  </footer>
</main>
</body>
</html>
```